New Sports Team- Womens Football

New team in San Diego.  Looking for a website that can be updated by us after the design is established.
Pages needed:
About us
Roster
Coaches/Staff
Schedule
Online Store (This link will go out to an external vendor)
Community Partners /Sponsors
Some good team pages to take a look at:
velmaroquills.com
brindlecoveotterball.com

Please use the logo I attempted to upload.  Looking for Flash Intro that incorporates the definition of the word "KESTO" and then the logo appearing.
Use the following words:
;any sudden, strong increase, as of energy, enthusiasm, etc.
;To improve one's performance suddenly, especially in bettering one's standing in a competition.

I placed a couple more pictures.
Adding another version of the team logo. In all designs I have seen thus far, everyone has the logo very small and it appears transparent. Might help to have the jpeg version. Also added some more photos
We are approaching the deadline quickly. Just a few last notes to the designs I have been viewing. All designs that are not close to the brief will be eliminated.

```html
<!DOCTYPE html>
<html lang="en">
<head>
<meta charset="utf-8">
<title>Kesto Bay Womens Football Club</title>
<link href="https://fonts.googleapis.com/css2?family=Arimo:wght@400;700&family=Open+Sans:wght@400;600&display=swap" rel="stylesheet">
<style>
:root{
  --navy:#0b2a6b;
  --navy-deep:#061c4c;
  --blue:#123a8a;
  --nav-active:#1d4fa6;
  --gold:#c7a43f;
  --text:#7a7a7a;
  --title:#14306e;
  --row-a:#d7dde6;
  --row-b:#e9edf2;
  --panel-line:#b9c2cf;
}
*{box-sizing:border-box;margin:0;padding:0}
html,body{width:1200px;height:1101px;overflow:hidden}
body{position:relative;font-family:"Arimo",Arial,sans-serif;background:#fff;color:var(--text)}
.abs{position:absolute}
.header{left:0;top:0;width:1200px;height:102px;background:repeating-linear-gradient(135deg,#f4f6f8 0 3px,#e9ecf0 3px 5px)}
.brand{left:210px;top:28px;display:flex;align-items:center;gap:10px;font-family:"Open Sans",sans-serif;font-weight:600;font-size:30px;color:var(--navy)}
.brand .mark{width:26px;height:26px;border-radius:50%;background:var(--navy)}
.promo{left:711px;top:11px;width:296px;height:81px;background:linear-gradient(90deg,#0a1f55 0 40%,#1a5fd0 70%,#0c2f8a);border:1px solid #0a1a44}
.promo .visit{left:12px;top:10px;color:#fff;font-weight:700;font-size:13px;line-height:18px}
.promo .shop{left:16px;top:52px;width:58px;height:20px;border-radius:4px;background:#17345f;color:#fff;font-size:11px;text-align:center;line-height:20px}
.promo .name{left:110px;top:20px;width:176px;color:#e0332a;font-weight:700;font-size:22px;line-height:24px;text-align:center}
.nav{left:0;top:102px;width:1200px;height:30px;background:linear-gradient(#163f94,var(--navy-deep))}
.nav ul{list-style:none;display:flex;position:absolute;left:196px;top:0}
.nav li{color:#fff;font-size:15px;line-height:30px;padding:0 10px;letter-spacing:.2px}
.nav li.active{background:var(--nav-active)}
.grass{left:0;top:132px;width:1200px;height:235px;background:linear-gradient(#4e8a22,#7fb04a 45%,#e6eee0 85%,#fff)}
.hero{left:179px;top:144px;width:524px;height:220px;background:linear-gradient(135deg,#2f3d6e,#4b3a86 45%,#6a7aa4 70%,#3f5a2d)}
.hero .tag{left:34px;top:172px;color:#fff;font-family:"Open Sans",sans-serif;font-weight:600;font-size:25px}
.dots{left:374px;top:180px;width:108px;height:16px;border-radius:8px;background:var(--navy-deep);display:flex;justify-content:space-around;align-items:center;padding:0 6px}
.dots i{width:7px;height:7px;border-radius:50%;background:#fff}
.panel{border:2px solid var(--panel-line);background:#fff}
.panel-title{background:linear-gradient(var(--blue),var(--navy-deep));color:#fff;font-family:"Open Sans",sans-serif;font-size:20px;text-align:center}
.tabs{display:flex;height:32px;align-items:center;font-size:12px;color:var(--title);background:linear-gradient(#fff,#eef1f5)}
.tabs span{padding:0 20px 0 24px;position:relative;line-height:32px}
.tabs span::after{content:"";position:absolute;right:0;top:0;width:10px;height:32px;border-right:1px solid var(--panel-line);transform:skewX(20deg)}
.offfield{left:711px;top:142px;width:296px;height:224px}
.offfield .panel-title{height:188px;padding-top:4px}
.thumbs{position:absolute;left:18px;top:44px;display:grid;grid-template-columns:repeat(4,50px);gap:26px 20px}
.thumbs div{width:50px;height:50px;border:2px solid #3c5b94;background:linear-gradient(135deg,#3d4f7a,#6b7f56)}
.item{position:absolute;left:191px;width:502px;border-bottom:2px dotted #c9cdd4}
.item .thumb{position:absolute;left:0;top:0;width:92px;height:92px}
.item .body{margin-left:114px}
.item h3{font-size:12px;font-weight:400;color:var(--title);letter-spacing:.3px}
.item time{display:block;font-size:9px;color:#333;margin:2px 0 8px}
.item p{font-size:11.5px;line-height:15px}
.item a{display:block;color:var(--gold);font-weight:700;font-size:12px;margin-top:1px;text-decoration:none}
.footlinks{left:191px;top:962px;font-size:11px;color:var(--title)}
.schedule{left:711px;top:393px;width:296px;height:357px}
.schedule .panel-title{height:33px;line-height:33px}
table{border-collapse:collapse;width:100%;font-size:12px}
th{height:29px;font-weight:400;color:var(--title);font-size:11px;background:#fff;border-bottom:1px solid var(--panel-line)}
td{height:29px;text-align:center;color:#111}
td.d{font-size:9px;width:70px}
td.r{width:68px;font-size:11px}
tr:nth-child(odd) td{background:var(--row-a)}
tr:nth-child(even) td{background:var(--row-b)}
td+td,th+th{border-left:2px solid var(--panel-line)}
td .at{color:#777}
.event{left:711px;top:767px;width:296px;height:209px}
.event .panel-title{position:relative;height:175px;padding-top:2px}
.badge{position:absolute;top:40px;width:88px;height:92px;background:#fff;border:2px solid #cdd3dd;display:flex;align-items:center;justify-content:center;color:var(--navy);font-family:"Open Sans",sans-serif;font-weight:600;font-size:15px;text-align:center}
.vs{position:absolute;left:104px;top:62px;width:80px;color:#fff;font-size:11px;font-weight:700;line-height:18px}
.vs b{display:block;font-size:18px;font-weight:400}
.event .rule{position:absolute;left:10px;right:10px;top:143px;border-top:2px dotted #7f96c4}
.event .when{position:absolute;left:0;right:0;top:152px;color:var(--gold);font-size:12px;font-weight:700;font-family:"Arimo",sans-serif}
.footer{left:0;top:993px;width:1200px;height:108px;background:repeating-linear-gradient(135deg,#f1f3f6 0 3px,#e6e9ee 3px 5px);border-top:1px solid #dde1e7}
.footer .brand{left:208px;top:24px}
.copy{left:405px;top:78px;color:var(--navy);font-size:13.5px}
</style>
</head>
<body>
<header class="abs header">
  <div class="abs brand"><span class="mark"></span>KESTO</div>
  <div class="abs promo">
    <div class="abs visit">VISIT THE<br>KESTO STORE</div>
    <div class="abs shop">SHOP</div>
    <div class="abs name">IRONLINE<br>TRAINING</div>
  </div>
</header>
<nav class="abs nav"><ul>
  <li>NEWS</li><li class="active">ABOUT US</li><li>ROSTER</li><li>COACHES</li><li>SHEDULE</li><li>ONLINE STORE</li><li>SPONSORS</li>
</ul></nav>
<div class="abs grass" role="img" aria-label="Close-up of green grass field"></div>
<section class="abs hero" role="img" aria-label="Players lined up at the line of scrimmage">
  <div class="abs tag">FEEL THE RUSH</div>
  <div class="abs dots"><i></i><i></i><i></i><i></i><i></i><i></i><i></i></div>
</section>
<aside class="abs panel offfield">
  <div class="panel-title">OFF THE FIELD
    <div class="thumbs">
      <div role="img" aria-label="Team photo"></div><div role="img" aria-label="Team photo"></div><div role="img" aria-label="Team photo"></div><div role="img" aria-label="Team photo"></div>
      <div role="img" aria-label="Team photo"></div><div role="img" aria-label="Team photo"></div><div role="img" aria-label="Team photo"></div><div role="img" aria-label="Team photo"></div>
    </div>
  </div>
  <div class="tabs"><span>Staff</span><span>Team</span></div>
</aside>
<main>
  <article class="item" style="top:391px;height:110px">
    <div class="thumb" role="img" aria-label="Players on the sideline" style="background:linear-gradient(135deg,#2a3a6e,#8a2f3a)"></div>
    <div class="body"><h3>LOREM IPSUM DOLOR SIT AMET</h3><time>09.12.2010 - 5:46 PM</time>
    <p>Lorem ipsum dolor sit amet, consectetur adipiscing elit. Nam sodales viverra velit ac pellentesque. Aenean accumsan turpis ut urna gravida ultricies et ut erat.</p><a>READ MORE</a></div>
  </article>
  <article class="item" style="top:515px;height:110px">
    <div class="thumb" role="img" aria-label="Coaches on the field" style="background:linear-gradient(135deg,#8aa0b8,#a03a3a 60%,#4f7a2c)"></div>
    <div class="body"><h3>LOREM IPSUM DOLOR SIT AMET</h3><time>09.12.2010 - 5:46 PM</time>
    <p>Lorem ipsum dolor sit amet, consectetur adipiscing elit. Nam sodales viverra velit ac pellentesque. Aenean accumsan turpis ut urna gravida ultricies et ut erat.Phasellus vel quam quis odio faucibus consectetur vitae eget elit.</p><a>READ MORE</a></div>
  </article>
  <article class="item" style="top:631px;height:110px">
    <div class="thumb" role="img" aria-label="Player running on the field" style="background:linear-gradient(135deg,#6e8a5a,#3b4a78 55%,#5f8a3c)"></div>
    <div class="body"><h3>LOREM IPSUM DOLOR SIT AMET</h3><time>09.12.2010 - 5:46 PM</time>
    <p>Lorem ipsum dolor sit amet, consectetur adipiscing elit. Nam sodales viverra velit ac pellentesque. Aenean accumsan turpis ut urna gravida ultricies et ut .</p><a>READ MORE</a></div>
  </article>
  <article class="item" style="top:753px;height:124px">
    <div class="thumb" role="img" aria-label="Game action on the field" style="background:linear-gradient(135deg,#4a5a3a,#3d4680 50%,#5a8a38)"></div>
    <div class="body"><h3>LOREM IPSUM DOLOR SIT AMET</h3><time>09.12.2010 - 5:46 PM</time>
    <p>Lorem ipsum dolor sit amet, consectetur adipiscing elit. Nam sodales viverra velit ac pellentesque. Aenean accumsan turpis ut urna gravida ultricies et ut erat.Phasellus vel quam quis odio faucibus consectetur vitae eget elit. Sed ultricies semper dui a scelerisque. Fusce sagittis semper quam.</p><a>READ MORE</a></div>
  </article>
</main>
<div class="abs footlinks">Home &nbsp;| &nbsp;News &nbsp;| &nbsp;About us &nbsp;| &nbsp;Roster &nbsp;| &nbsp;Coaches &nbsp;| &nbsp;Shedule &nbsp;| &nbsp;Online Store &nbsp;| &nbsp;Sponsors</div>
<aside class="abs panel schedule">
  <div class="panel-title">SHEDULE</div>
  <table>
    <thead><tr><th>DATE</th><th>GAME</th><th>RESULT</th></tr></thead>
    <tbody>
      <tr><td class="d">09.12.2010</td><td><span class="at">at</span> OPPONENT</td><td class="r">W 17 - 9</td></tr>
      <tr><td class="d">09.12.2010</td><td><span class="at">at</span> OPPONENT</td><td class="r">W 17 - 9</td></tr>
      <tr><td class="d">09.12.2010</td><td><span class="at">at</span> OPPONENT</td><td class="r">W 17 - 9</td></tr>
      <tr><td class="d">09.12.2010</td><td><span class="at">at</span> OPPONENT</td><td class="r">W 17 - 9</td></tr>
      <tr><td class="d">09.12.2010</td><td><span class="at">at</span> OPPONENT</td><td class="r">W 17 - 9</td></tr>
      <tr><td class="d">09.12.2010</td><td><span class="at">at</span> OPPONENT</td><td class="r">W 17 - 9</td></tr>
      <tr><td class="d">09.12.2010</td><td><span class="at">at</span> OPPONENT</td><td class="r">W 17 - 9</td></tr>
      <tr><td class="d">09.12.2010</td><td><span class="at">at</span> OPPONENT</td><td class="r">W 17 - 9</td></tr>
      <tr><td class="d">09.12.2010</td><td><span class="at">at</span> OPPONENT</td><td class="r">L 17 - 9</td></tr>
    </tbody>
  </table>
  <div class="tabs"><span>Full Shedule</span></div>
</aside>
<aside class="abs panel event">
  <div class="panel-title">EVENT
    <div class="badge" style="left:10px">KESTO</div>
    <div class="vs">KESTO<b>AT</b>OPPONENT</div>
    <div class="badge" style="left:196px">HARBOR HAWKS</div>
    <div class="rule"></div>
    <div class="when">09.12.2010 / BAYFRONT STADIUM / 8:00 PM</div>
  </div>
  <div class="tabs"><span>Roster</span><span>All Upcoming Events</span></div>
</aside>
<footer class="abs footer">
  <div class="abs brand"><span class="mark"></span>KESTO</div>
  <div class="abs copy">Copyright © &nbsp;Kesto Bay Womens Football Club | All rights reserved.</div>
</footer>
</body>
</html>
```